Need sign/billboard help

I need somone to take my logo and turn it into a sign.
Needs to have: Bright Paws
Canine Play & Care Center
319-572-8134
Daycare - Boarding - Learning
Colors to use are in the pictures i included, however feel free to use different shades of gray. i Don't necessary want to background to be one solid color.
Also this sing will be a rectangle (4'x8')
Daycare

```html
<!DOCTYPE html>
<html lang="en">
<head>
<meta charset="utf-8">
<title>Bright Paws – Sign</title>
<link rel="stylesheet" href="https://fonts.googleapis.com/css2?family=Archivo+Black&display=swap">
<style>
  :root {
    --page-bg: #0f1b33;
    --lime: #c3d43a;
    --lime-deep: #a8bb27;
    --ink: #151515;
    --charcoal: #242223;
    --white: #ffffff;
  }
  html, body {
    margin: 0;
    padding: 0;
    width: 1197px;
    height: 1200px;
    overflow: hidden;
    background: var(--page-bg);
  }
  .stage {
    width: 1197px;
    height: 1200px;
    display: flex;
    align-items: center;
    justify-content: center;
  }
  .sign {
    width: 1100px;
    height: 555px;
    display: block;
  }
  .services-text,
  .brand-name,
  .brand-subtitle,
  .phone-number {
    font-family: "Archivo Black", "Arial Black", sans-serif;
  }
  .services-text { fill: var(--ink); font-size: 46px; }
  .brand-name { fill: var(--ink); font-size: 72px; }
  .brand-subtitle { fill: var(--ink); font-size: 22px; }
  .phone-number { fill: var(--lime); font-size: 84px; }
  .paw { fill: var(--white); }
</style>
</head>
<body>
<main class="stage">
  <svg class="sign" viewBox="0 0 1100 555" xmlns="http://www.w3.org/2000/svg" aria-label="Bright Paws sign">
    <defs>
      <pattern id="steel-stripes" width="10" height="555" patternUnits="userSpaceOnUse">
        <rect width="10" height="555" fill="#8a8c8f"/>
        <rect x="0" width="4" height="555" fill="#9a9c9f"/>
        <rect x="7" width="1" height="555" fill="#77797c"/>
      </pattern>
      <radialGradient id="steel-glow" cx="0.5" cy="0.42" r="0.55">
        <stop offset="0" stop-color="#ffffff" stop-opacity="0.75"/>
        <stop offset="0.55" stop-color="#ffffff" stop-opacity="0.2"/>
        <stop offset="1" stop-color="#000000" stop-opacity="0.25"/>
      </radialGradient>
      <linearGradient id="lime-band" x1="0" y1="0" x2="0" y2="1">
        <stop offset="0" stop-color="#cbdc45"/>
        <stop offset="1" stop-color="#a8bb27"/>
      </linearGradient>
      <symbol id="paw-icon" viewBox="0 0 24 24">
        <ellipse cx="12" cy="16" rx="6" ry="5"/>
        <ellipse cx="5" cy="10" rx="2.4" ry="3"/>
        <ellipse cx="9.5" cy="5.5" rx="2.4" ry="3"/>
        <ellipse cx="14.5" cy="5.5" rx="2.4" ry="3"/>
        <ellipse cx="19" cy="10" rx="2.4" ry="3"/>
      </symbol>
    </defs>

    <rect class="steel-panel" x="0" y="0" width="1100" height="555" fill="url(#steel-stripes)"/>
    <rect x="0" y="0" width="1100" height="555" fill="url(#steel-glow)"/>

    <rect class="services-band" x="0" y="0" width="1100" height="86" fill="url(#lime-band)"/>
    <rect class="services-rule" x="0" y="86" width="1100" height="9" fill="var(--ink)"/>
    <text class="services-text" x="35" y="62" textLength="290" lengthAdjust="spacingAndGlyphs">DAYCARE</text>
    <use class="paw" href="#paw-icon" x="341" y="30" width="29" height="29"/>
    <text class="services-text" x="378" y="62" textLength="328" lengthAdjust="spacingAndGlyphs">BOARDING</text>
    <use class="paw" href="#paw-icon" x="718" y="30" width="29" height="29"/>
    <text class="services-text" x="761" y="62" textLength="312" lengthAdjust="spacingAndGlyphs">LEARNING</text>

    <text class="brand-name" x="550" y="258" text-anchor="middle" textLength="560" lengthAdjust="spacingAndGlyphs">BRIGHT PAWS</text>
    <text class="brand-subtitle" x="550" y="306" text-anchor="middle" textLength="480" lengthAdjust="spacingAndGlyphs">CANINE PLAY &amp; CARE CENTER</text>

    <path class="lime-arc" d="M0 502 Q 560 340 1100 478 L1100 555 L0 555 Z" fill="var(--lime)"/>
    <path class="phone-band" d="M0 516 Q 560 354 1100 492 L1100 555 L0 555 Z" fill="var(--charcoal)"/>
    <text class="phone-number" x="554" y="527" text-anchor="middle" textLength="723" lengthAdjust="spacingAndGlyphs">319.572.8134</text>
  </svg>
</main>
</body>
</html>
```